Real Estate Sign 2

Our company is called Harwick Tolland Realty. We are a real estate development company. We need a sign that we are going to hang outside of our projects that says: Another project brought to you by Harwick Tolland Realty... For Sale....(213) 555-0847. At the very bottom is needs to say CaBRE# 04736291" We want the Harwick Tolland Realty to be sophisticated, fresh, simple. We do not have a logo so maybe one can be incorporated into the sign. Sign will be about 30"x24"

Industry/Entity Type

Real Estate

```html
<!DOCTYPE html>
<html lang="en">
<head>
<meta charset="UTF-8">
<title>Harwick Tolland Realty – Project Sign</title>
<link rel="stylesheet" href="https://fonts.googleapis.com/css2?family=EB+Garamond:wght@400&family=Great+Vibes&display=swap">
<style>
  :root {
    --ink: #111111;
    --paper: #ffffff;
  }
  * { margin: 0; padding: 0; box-sizing: border-box; }
  html, body {
    width: 1200px;
    height: 900px;
    overflow: hidden;
    background: var(--paper);
  }
  .sign {
    position: relative;
    width: 1200px;
    height: 900px;
    background: var(--paper);
    color: var(--ink);
    font-family: "EB Garamond", "Garamond", serif;
    text-align: center;
  }
  .sign > * {
    position: absolute;
    left: 0;
    width: 100%;
  }
  .sign__intro {
    top: 38px;
    font-size: 52px;
    line-height: 1;
    letter-spacing: 0.5px;
  }
  .sign__company {
    top: 120px;
    font-family: "Great Vibes", cursive;
    font-weight: 400;
    line-height: 1;
  }
  .sign__company-name {
    display: block;
    font-size: 150px;
  }
  .sign__company-suffix {
    display: block;
    font-size: 130px;
    margin-top: 10px;
  }
  .sign__divider {
    top: 482px;
    left: 400px;
    width: 400px;
    height: 50px;
  }
  .sign__status {
    top: 572px;
    font-size: 94px;
    line-height: 1;
  }
  .sign__phone {
    top: 668px;
    font-size: 100px;
    line-height: 1;
  }
  .sign__license {
    top: 826px;
    font-size: 42px;
    line-height: 1;
  }
</style>
</head>
<body>
  <main class="sign">
    <p class="sign__intro">Another project brought to you by</p>
    <h1 class="sign__company">
      <span class="sign__company-name">Harwick Tolland</span>
      <span class="sign__company-suffix">Realty</span>
    </h1>
    <svg class="sign__divider" viewBox="0 0 400 50" role="img" aria-label="Ornamental flourish divider">
      <rect x="0" y="24" width="400" height="2" fill="var(--ink)"/>
    </svg>
    <p class="sign__status">For Sale</p>
    <p class="sign__phone">(213) 555-0847</p>
    <p class="sign__license">CaBRE# 04736291</p>
  </main>
</body>
</html>
```